Creating a visual for the various stage of our Packets by Locations: *Memphis Region *Clinics in TRV School District*Nashville Region *Knoxville Region. The attached file contains two tabs the layout of the packet scheme that currently in place and a second tab with the definition of the various cells that is needed as a legend on each report. The goal is to get the report tab an easily "eye" visual for the CEO of the company to follow. Create a Reporting Dashboard Template that we can input number into easily to update. The color scheme should reflect our website www.brightsprout.example
Target Market(s)
Pediatric company that performs BrightSprout Exams and Optometry exams in school districts
Industry/Entity Type
Healthcare
Requirements
Must have
- Printable dash page. You can use this file and add a dash page that flows from the report page as an option in excel
Nice to have
- maybe 3D modern feel with the color scheme of the company website

```html
<!DOCTYPE html>
<html lang="en">
<head>
<meta charset="utf-8">
<title>BrightSprout Packet Report</title>
<link rel="stylesheet" href="https://fonts.googleapis.com/css2?family=Tinos:ital,wght@0,400;0,700;1,400&display=swap">
<style>
  :root {
    --brand: #5b8fc9;
    --brand-soft: #7fa7d6;
    --navy: #203a6e;
    --navy-deep: #1a2f5c;
    --band: #6d93c9;
    --band-light: #a9c3e6;
    --ink: #111;
    --grid: #8a8a8a;
    --paper: #ffffff;
    --wash-top: #e3eef8;
    --wash-mid: #cfe0f2;
  }
  * { box-sizing: border-box; margin: 0; padding: 0; }
  html, body { width: 859px; height: 1200px; overflow: hidden; }
  body {
    font-family: "Tinos", "Times New Roman", serif;
    color: var(--ink);
    background: var(--paper);
  }
  .page {
    position: relative;
    width: 859px; height: 1200px;
    background: linear-gradient(180deg, var(--paper) 0, var(--paper) 250px, var(--wash-top) 290px, var(--wash-mid) 650px, var(--wash-top) 1000px, #eef5fb 1200px);
    overflow: hidden;
  }
  .page::before {
    content: ""; position: absolute; left: -100px; top: 250px; width: 1100px; height: 140px;
    background: linear-gradient(180deg, rgba(255,255,255,0.75), rgba(255,255,255,0));
    transform: rotate(-3deg);
  }
  .brand {
    position: absolute; left: 250px; top: 72px;
    display: flex; align-items: center; gap: 14px;
  }
  .brand-dot { width: 40px; height: 40px; border-radius: 50%; background: var(--brand); }
  .brand-name { font-size: 66px; font-weight: 700; color: var(--brand); letter-spacing: -1px; line-height: 1; }
  .tagline {
    position: absolute; right: 58px; top: 212px; text-align: right;
    font-style: italic; color: var(--brand-soft); line-height: 1.1;
  }
  .tagline span { display: block; }
  .tagline .lead { margin-right: 62px; font-size: 20px; }
  .tagline .tail { font-size: 23px; }
  .report { position: absolute; left: 97px; width: 665px; z-index: 1; }
  table { width: 100%; border-collapse: collapse; table-layout: fixed; border: 2px solid #000; background: #fff; font-size: 12px; }
  col.label { width: 326px; }
  col.num { width: 163px; }
  td, th { border: 1px solid var(--grid); padding: 0 6px; height: 18.5px; line-height: 1.1; }
  td.n { text-align: right; }
  th.head-row { background: linear-gradient(180deg, #2b4a85, var(--navy-deep)); color: #fff; font-weight: 400; height: 77px; font-size: 12.5px; text-align: center; }
  .title td { font-weight: 700; }
  .band td { background: var(--band); font-weight: 700; }
  .dark td { background: var(--navy); color: #fff; font-weight: 700; }
  .soft td.n { background: var(--band-light); }
  .tall td { height: 36px; font-weight: 700; vertical-align: middle; }
  .sec-head { top: 298px; }
  .sec-ax { top: 380px; }
  .sec-ins { top: 616px; }
  .sec-ins td { height: 19px; }
  .sec-exam { top: 745px; }
  .sec-exam .band td { height: 38px; vertical-align: bottom; padding-bottom: 2px; }
  .sec-cmp { top: 834px; }
  .sec-cmp td { height: 20px; }
  .sec-cmp .tall td { height: 38px; }
  .sec-need { top: 950px; }
  .sec-need table { font-size: 15px; }
  .sec-need td { height: 37px; font-weight: 700; letter-spacing: 0.3px; }
  .sec-need col.wide { width: 489px; }
  .sec-need col.val { width: 176px; }
  .footer {
    position: absolute; right: 59px; top: 1150px;
    font-size: 24px; color: var(--brand-soft);
  }
</style>
</head>
<body>
<main class="page">
  <div class="brand">
    <div class="brand-dot"></div>
    <div class="brand-name">BrightSprout</div>
  </div>
  <p class="tagline"><span class="lead">Healthy Bodies Promote</span><span class="tail">Healthy Minds</span></p>

  <section class="report sec-head">
    <table>
      <colgroup><col class="label"><col class="num"><col class="num"></colgroup>
      <tr><th class="head-row">Name/Clinic</th><th class="head-row">Nashville/Knoxville</th><th class="head-row">Memphis Clinic</th></tr>
    </table>
  </section>

  <section class="report sec-ax">
    <table>
      <colgroup><col class="label"><col class="num"><col class="num"></colgroup>
      <tr class="title"><td colspan="3">AX System vs. Packet Tracking System</td></tr>
      <tr><td>Call Center Packets</td><td class="n">69</td><td class="n">13984</td></tr>
      <tr><td>Complete Packets</td><td class="n">22656</td><td class="n">15865</td></tr>
      <tr><td>Duplicates Packets</td><td class="n">668</td><td class="n">2776</td></tr>
      <tr><td>Incomplete Packets</td><td class="n">919</td><td class="n">1666</td></tr>
      <tr><td>No Signature Packets</td><td class="n">0</td><td class="n">0</td></tr>
      <tr><td>Decline Packets</td><td class="n">1036</td><td class="n">2776</td></tr>
      <tr><td>Enable Packets</td><td class="n">489</td><td class="n">286</td></tr>
      <tr class="band"><td>Total Packets</td><td class="n">25364</td><td class="n">29817</td></tr>
      <tr class="band"><td>Packets Tracking System</td><td class="n">23349</td><td class="n">37469</td></tr>
      <tr class="dark"><td>(Over)/Under Estimated</td><td class="n">2015</td><td class="n">-7582</td></tr>
    </table>
  </section>

  <section class="report sec-ins">
    <table>
      <colgroup><col class="label"><col class="num"><col class="num"></colgroup>
      <tr class="title"><td colspan="3">Insured Packets</td></tr>
      <tr><td>Call Center Packets</td><td class="n">69</td><td class="n">13984</td></tr>
      <tr><td>Complete Packets</td><td class="n">22605</td><td class="n">15865</td></tr>
      <tr><td>Incomplete Packets</td><td class="n">0</td><td class="n">1666</td></tr>
      <tr class="band"><td>Uninsured Packets</td><td class="n">5944</td><td class="n">7361</td></tr>
      <tr class="band"><td>Insured Packets</td><td class="n">16538</td><td class="n">22466</td></tr>
    </table>
  </section>

  <section class="report sec-exam">
    <table>
      <colgroup><col class="label"><col class="num"><col class="num"></colgroup>
      <tr class="band soft"><td>Insured completed exams out of completed packets</td><td class="n">3718</td><td class="n">6107</td></tr>
      <tr class="band"><td>Left Behind to Complete</td><td class="n">12792</td><td class="n">16359</td></tr>
    </table>
  </section>

  <section class="report sec-cmp">
    <table>
      <colgroup><col class="label"><col class="num"><col class="num"></colgroup>
      <tr class="tall"><td>Comparison of Insured Packets 2017-18 vs. 2018-19</td><td></td><td></td></tr>
      <tr><td>2017-2018</td><td class="n">22356</td><td class="n">30538</td></tr>
      <tr><td>2018-2019</td><td class="n">16510</td><td class="n">22466</td></tr>
      <tr class="band"><td></td><td class="n">-5844</td><td class="n">-8072</td></tr>
    </table>
  </section>

  <section class="report sec-need">
    <table>
      <colgroup><col class="wide"><col class="val"></colgroup>
      <tr><td colspan="2">Combined Need Analysis MEM &amp; NASH/KNOX</td></tr>
      <tr><td>Total gross packets received statewide</td><td class="n">55191</td></tr>
      <tr><td>Total Insured packets received statewide</td><td class="n">38976</td></tr>
      <tr><td>Statewide EPSDT Needs for Insured Packets</td><td class="n">-13916</td></tr>
      <tr><td>Gross Packet Needs to convert into Insured Packets</td><td class="n">-17951.64</td></tr>
    </table>
  </section>

  <p class="footer">Innovators in School Health Care Services</p>
</main>
</body>
</html>
```